Ready to Run a Venture? Podcast

We need a "Podcast Cover" for inclusion on Vexora and brightreef along with a matching or complimentary banner to be included on a landing page which will be hosted on Plinkfern (a Plinkfern template). The Podcast is called the "Ready to Run a Venture?" Podcast and has a tag line of "listen before you leap".

I've included an image for a bit of inspiration that shows a person ready to leap into the unknown which, in our podcast, is like a metaphor for launching a business. You may use the photo in your design if you wish or do something completely different including "cartoon" characters or simply text.

Target Market(s)

People who are thinking about starting a new business or buying an existing business and whom have never owned a business before.

Industry/Entity Type

Startup

Font styles to use
Sans Serif

Colors

Designer to choose colors to be used in the design.

Requirements
Must have
• incorporate the "listen before you leap" tagline.

```html
<!DOCTYPE html>
<html lang="en">
<head>
<meta charset="utf-8">
<title>Ready to Run a Venture? Podcast Cover</title>
<link rel="stylesheet" href="https://fonts.googleapis.com/css2?family=Roboto+Condensed:wght@700&family=Open+Sans:wght@600&display=swap">
<style>
  :root {
    --frame: #333333;
    --paper: #fbfbfb;
    --paper-edge: #f1f1f1;
    --ink: #1c1c1c;
    --ink-soft: #2b2b2b;
    --ink-grey: #5a5a5a;
    --pill-start: #22b573;
    --pill-end: #29abe2;
    --white: #ffffff;
    --mesh-tone: #e4e4e4;
  }
  html, body {
    margin: 0;
    padding: 0;
    width: 1200px;
    height: 1200px;
    overflow: hidden;
    background: var(--frame);
  }
  .cover {
    position: relative;
    width: 1200px;
    height: 1200px;
    box-sizing: border-box;
    border: 15px solid var(--frame);
    background: radial-gradient(circle at 50% 30%, var(--paper) 0%, var(--paper-edge) 100%);
    overflow: hidden;
  }
  .mesh-backdrop {
    position: absolute;
    left: 0;
    right: 0;
    top: 265px;
    bottom: 0;
    background: linear-gradient(180deg, rgba(228,228,228,0) 0%, rgba(228,228,228,0.45) 45%, rgba(228,228,228,0.6) 100%);
  }
  .platform {
    position: absolute;
    left: 74px;
    top: 108px;
    display: flex;
    align-items: center;
    gap: 14px;
  }
  .platform-dot {
    width: 50px;
    height: 50px;
    border-radius: 50%;
    background: var(--ink);
  }
  .platform-name {
    font-family: "Open Sans", sans-serif;
    font-weight: 600;
    font-size: 56px;
    line-height: 1;
    color: var(--ink);
    letter-spacing: -1px;
  }
  .headline {
    position: absolute;
    left: 0;
    right: 0;
    top: 350px;
    margin: 0;
    text-align: center;
    font-family: "Roboto Condensed", sans-serif;
    font-weight: 700;
    font-size: 128px;
    line-height: 1;
    letter-spacing: -2px;
    background: linear-gradient(90deg, var(--ink-grey) 20%, var(--ink) 55%);
    -webkit-background-clip: text;
    background-clip: text;
    color: transparent;
  }
  .title-pill {
    position: absolute;
    left: 253px;
    top: 490px;
    width: 690px;
    height: 194px;
    border-radius: 97px;
    background: linear-gradient(90deg, var(--pill-start), var(--pill-end));
    display: flex;
    align-items: center;
    justify-content: center;
  }
  .title-word {
    font-family: "Roboto Condensed", sans-serif;
    font-weight: 700;
    font-size: 166px;
    line-height: 1;
    color: var(--white);
    letter-spacing: -2px;
    margin-top: 6px;
  }
  .tagline {
    position: absolute;
    left: 0;
    right: 0;
    top: 935px;
    margin: 0;
    text-align: center;
    font-family: "Roboto Condensed", sans-serif;
    font-weight: 700;
    font-size: 108px;
    line-height: 1;
    letter-spacing: -2px;
    color: var(--ink-soft);
  }
</style>
</head>
<body>
  <main class="cover">
    <div class="mesh-backdrop" role="img" aria-label="Light grey geometric line mesh rising like a mountain range"></div>

    <div class="platform">
      <span class="platform-dot"></span>
      <span class="platform-name">Vexora</span>
    </div>

    <h1 class="headline">Ready to Run a</h1>

    <div class="title-pill">
      <span class="title-word">Venture</span>
    </div>

    <p class="tagline">listen before you leap</p>
  </main>
</body>
</html>
```